Stationery Design needed for logo design project

This project is linked to Logo: brand identity for modern furniture design studio..

Our company needs a Stationery Design. Please refer to our original project in the link above.

```html
<!DOCTYPE html>
<html lang="en">
<head>
<meta charset="utf-8">
<title>Vellmo Stationery</title>
<link href="https://fonts.googleapis.com/css2?family=Roboto+Condensed:wght@300;400;700&display=swap" rel="stylesheet">
<style>
  :root {
    --charcoal: #4a4a4a;
    --charcoal-dark: #444444;
    --paper: #ffffff;
    --paper-soft: #f4f4f4;
    --ink: #2e2e2e;
    --backdrop: #e4e4e2;
  }
  * { margin: 0; padding: 0; box-sizing: border-box; }
  html, body { width: 1200px; height: 1175px; overflow: hidden; }
  body {
    position: relative;
    background: var(--backdrop);
    font-family: "Roboto Condensed", Arial, sans-serif;
    color: var(--ink);
  }
  .wordmark {
    font-family: "Roboto Condensed", Arial, sans-serif;
    font-weight: 300;
    letter-spacing: 1px;
    line-height: 1;
  }
  .contact { display: flex; align-items: center; gap: 6px; white-space: nowrap; }
  .contact svg { flex: none; }

  /* Business card */
  .card {
    position: absolute; left: 100px; top: 303px; width: 638px; height: 823px;
    background: var(--charcoal);
  }
  .card__band {
    position: absolute; left: 0; top: 674px; width: 100%; height: 48px;
    background: var(--paper);
  }
  .card__band .wordmark {
    position: absolute; left: 53px; top: 4px; font-size: 40px; color: var(--charcoal);
  }
  .card__contacts {
    position: absolute; left: 53px; top: 730px;
    display: grid; grid-template-columns: 146px auto; row-gap: 8px;
    font-size: 13px; color: var(--paper);
  }

  /* Letterhead */
  .letterhead {
    position: absolute; left: 206px; top: 98px; width: 639px; height: 825px;
    background: linear-gradient(180deg, var(--paper) 0%, var(--paper-soft) 100%);
  }
  .letterhead__spine {
    position: absolute; left: 0; top: 0; width: 54px; height: 760px;
    background: var(--charcoal);
    border-bottom-right-radius: 18px;
  }
  .letterhead .wordmark {
    position: absolute; left: 94px; top: 52px; font-size: 46px; color: var(--charcoal);
  }
  .letter {
    position: absolute; left: 94px; top: 150px; width: 474px;
    font-size: 12px; line-height: 18px; color: var(--ink);
  }
  .letter p { margin: 0; }
  .letter .gap { margin-top: 18px; }
  .letter .justify { text-align: justify; }
  .signature {
    position: absolute; left: 94px; top: 648px;
    font-size: 12px; line-height: 18px;
  }
  .signature strong { font-weight: 700; }
  .letterhead__contacts {
    position: absolute; left: 54px; top: 780px; width: 540px;
    display: flex; justify-content: space-between;
    font-size: 10px; color: var(--ink);
  }

  /* Envelope */
  .envelope {
    position: absolute; left: 456px; top: 530px; width: 713px; height: 312px;
    background: linear-gradient(180deg, var(--paper-soft) 0%, var(--paper) 100%);
    box-shadow: 0 0 0 1px #d8d8d8;
  }
  .envelope__band {
    position: absolute; left: 0; top: 204px; width: 100%; height: 33px;
    background: var(--charcoal-dark);
  }
  .envelope__band .wordmark {
    position: absolute; left: 32px; top: 1px; font-size: 34px; color: var(--paper);
  }
  .envelope__contacts {
    position: absolute; left: 34px; top: 247px;
    display: grid; grid-template-columns: 146px auto; row-gap: 6px;
    font-size: 12.5px; color: var(--ink);
  }
</style>
</head>
<body>

<svg width="0" height="0" style="position:absolute">
  <defs>
    <symbol id="icon-phone" viewBox="0 0 16 16">
      <circle cx="8" cy="8" r="8" fill="currentColor"/>
      <path d="M5.2 3.8l1.6 1.9-.9 1.1c.5 1.2 1.2 1.9 2.4 2.4l1.1-.9 1.9 1.6-.8 1.4c-3.3-.3-6.2-3.2-6.5-6.5z" fill="var(--icon-fg)"/>
    </symbol>
    <symbol id="icon-mail" viewBox="0 0 16 16">
      <circle cx="8" cy="8" r="8" fill="currentColor"/>
      <rect x="4" y="5.2" width="8" height="5.6" rx="0.6" fill="none" stroke="var(--icon-fg)" stroke-width="1"/>
      <path d="M4.2 5.6L8 8.4l3.8-2.8" fill="none" stroke="var(--icon-fg)" stroke-width="1"/>
    </symbol>
    <symbol id="icon-dot" viewBox="0 0 16 16">
      <circle cx="8" cy="8" r="8" fill="currentColor"/>
    </symbol>
  </defs>
</svg>

<section class="card" style="--icon-fg: var(--charcoal)">
  <div class="card__band"><span class="wordmark">vellmo</span></div>
  <div class="card__contacts">
    <span class="contact"><svg width="14" height="14" style="color:#fff"><use href="#icon-phone"/></svg>555 210 4870</span>
    <span class="contact"><svg width="14" height="14" style="color:#fff"><use href="#icon-dot"/></svg>social.example/vellmo</span>
    <span class="contact"><svg width="14" height="14" style="color:#fff"><use href="#icon-mail"/></svg>hello@vellmo.example</span>
    <span class="contact"><svg width="14" height="14" style="color:#fff"><use href="#icon-dot"/></svg>updates.example/vellmo</span>
  </div>
</section>

<section class="letterhead" style="--icon-fg: #fff">
  <div class="letterhead__spine"></div>
  <span class="wordmark">vellmo</span>
  <div class="letter">
    <p>April 15, 2009</p>
    <p>Ref. No.Appt/2009/4/VM0212</p>
    <p class="gap">&nbsp;Mr. Arjun Mehra</p>
    <p>C-17, Lotus Lane,</p>
    <p>Rampura, Jaipur</p>
    <p class="gap">Dear Mr. Mehra,</p>
    <p class="justify">With reference to your application and subsequent interview with us, we are pleased to appoint you as Sr. Graphic/Web Designer in our organization on the following terms and conditions.</p>
    <p>Joining Date: Your date of Joining would be 15/04/09.</p>
    <p class="justify">Salary: Your Annual Total Employment Cost to the company would be 1,80,000/- (One Lac Eighty Thousand) only.</p>
    <p class="justify">Place/Transfer: Your present place of work will be at Jaipur, but during the course of the service, you shall be liable to be posted / transferred anywhere to serve any of the Company's Projects or any other establishment in India or outside, at the sole discretion of the Management.</p>
    <p class="justify">Probation/Confirmation: You will be on probation for six months. Based on your performance your services will be confirmed in writing.</p>
    <p class="gap justify">During the probation period your services can be ended by either party without any reasons whatsoever. Upon completion you will be confirmed in the present position with one month's notice on either side.</p>
  </div>
  <div class="signature">
    <p><strong>Mr. Ravi Kapoor</strong></p>
    <p>C-17, Lotus Lane,</p>
    <p>Rampura, Jaipur</p>
  </div>
  <div class="letterhead__contacts" style="--icon-fg:#fff">
    <span class="contact"><svg width="12" height="12" style="color:var(--charcoal)"><use href="#icon-phone"/></svg>555 210 4870</span>
    <span class="contact"><svg width="12" height="12" style="color:var(--charcoal)"><use href="#icon-mail"/></svg>hello@vellmo.example</span>
    <span class="contact"><svg width="12" height="12" style="color:var(--charcoal)"><use href="#icon-dot"/></svg>social.example/vellmo</span>
    <span class="contact"><svg width="12" height="12" style="color:var(--charcoal)"><use href="#icon-dot"/></svg>updates.example/vellmo</span>
  </div>
</section>

<section class="envelope" style="--icon-fg:#fff">
  <div class="envelope__band"><span class="wordmark">vellmo</span></div>
  <div class="envelope__contacts">
    <span class="contact"><svg width="14" height="14" style="color:var(--charcoal)"><use href="#icon-phone"/></svg>555 210 4870</span>
    <span class="contact"><svg width="14" height="14" style="color:var(--charcoal)"><use href="#icon-dot"/></svg>social.example/vellmo</span>
    <span class="contact"><svg width="14" height="14" style="color:var(--charcoal)"><use href="#icon-mail"/></svg>hello@vellmo.example</span>
    <span class="contact"><svg width="14" height="14" style="color:var(--charcoal)"><use href="#icon-dot"/></svg>updates.example/vellmo</span>
  </div>
</section>

</body>
</html>
```